Bright Lane Collective needs updated website.

Our current website was designed on wix.com. (www.brightlanecollective.example).
We would like something a little more customized for what our company offers. Bright Lane Collective is a company specializing in connecting consumers with trustworthy and affordable service professionals. We need the website to be approachable and easy to use, while conveying our "Bright Lane" reputation.
Reason: Our project is now guaranteed. Please send your ideas. Thank you!
Target Market(s)
Homeowners
Industry/Entity Type
It Company
Look and feel

```html
<!DOCTYPE html>
<html lang="en">
<head>
<meta charset="utf-8">
<title>About Us – Bright Lane Collective</title>
<link rel="stylesheet" href="https://fonts.googleapis.com/css2?family=Source+Sans+3:wght@400;600;700&display=swap">
<style>
  :root {
    --green: #7cb32b;
    --green-dark: #58880f;
    --green-light: #c6ea8c;
    --ink: #3a3a3a;
    --ink-soft: #555555;
    --rule: #d6d6d6;
    --nav-rule: #8dbb3f;
    --white: #ffffff;
  }
  * { margin: 0; padding: 0; box-sizing: border-box; }
  html, body { width: 1200px; height: 980px; overflow: hidden; background: var(--white); }
  body { font-family: "Source Sans 3", "Myriad Pro", sans-serif; color: var(--ink); position: relative; }

  .site-header { position: absolute; left: 0; top: 0; width: 1200px; height: 166px; }
  .brand { position: absolute; left: 104px; top: 58px; display: flex; align-items: center; gap: 14px; }
  .brand-dot { width: 52px; height: 52px; border-radius: 50%; background: var(--green); }
  .brand-name { font-size: 34px; font-weight: 700; color: var(--ink); letter-spacing: -0.5px; }
  .call-box { position: absolute; right: 106px; top: 48px; }
  .call-label { font-size: 24px; font-weight: 400; color: var(--ink); line-height: 1.2; }
  .call-number { font-size: 31px; font-weight: 700; color: var(--ink); line-height: 1.2; margin-top: 2px; }

  .main-nav { position: absolute; left: 0; top: 166px; width: 1200px; height: 71px;
    border-top: 1px solid var(--nav-rule); border-bottom: 1px solid var(--rule); }
  .nav-item { position: absolute; top: 0; height: 69px; line-height: 66px; font-size: 21px;
    text-transform: uppercase; color: #555; text-align: center; text-decoration: none; }
  .nav-item.is-active { background: var(--green); color: var(--white); font-weight: 700; }
  .nav-sep { position: absolute; top: 20px; height: 28px; border-left: 1px dotted #bbb; }

  .page-title { position: absolute; left: 104px; top: 278px; font-size: 37px; font-weight: 700;
    color: var(--green); text-transform: uppercase; letter-spacing: -0.2px; }
  .about-photo { position: absolute; left: 105px; top: 361px; width: 299px; height: 211px;
    background: linear-gradient(180deg, #8fb6de 0%, #c9d9ea 38%, #9c8a55 58%, #c2a45c 100%); }
  .lead { position: absolute; left: 417px; top: 357px; width: 680px; font-size: 17.5px; font-weight: 700;
    line-height: 21px; color: var(--green); text-transform: uppercase; }
  .intro-text { position: absolute; left: 417px; top: 424px; width: 675px; font-size: 13.6px;
    line-height: 21.7px; color: var(--ink); }
  .section-title { position: absolute; left: 104px; top: 594px; font-size: 23px; font-weight: 400; color: var(--green); }
  .body-text { position: absolute; left: 104px; top: 646px; width: 990px; font-size: 13.4px;
    line-height: 22px; color: var(--ink); }

  .site-footer { position: absolute; left: 0; top: 748px; width: 1200px; height: 232px; background: var(--green-dark); color: var(--white); }
  .footer-brand { position: absolute; left: 105px; top: 47px; display: flex; align-items: center; gap: 10px; }
  .footer-brand .brand-dot { width: 44px; height: 44px; background: var(--white); }
  .footer-brand .brand-name { font-size: 24px; color: var(--white); }
  .copyright { position: absolute; left: 106px; top: 115px; font-size: 13.5px; }
  .footer-nav { position: absolute; right: 105px; top: 34px; display: flex; gap: 29px; font-size: 13.5px; }
  .footer-nav a { color: var(--white); text-decoration: none; }
  .footer-address { position: absolute; right: 104px; top: 81px; font-size: 17.5px; }
  .footer-phone { position: absolute; right: 104px; top: 124px; font-size: 22px; color: var(--green-light); }
  .footer-email { position: absolute; right: 104px; top: 153px; font-size: 17.5px; }
</style>
</head>
<body>
  <header class="site-header">
    <div class="brand"><span class="brand-dot"></span><span class="brand-name">Bright Lane Collective</span></div>
    <div class="call-box">
      <div class="call-label">Call Us Now:</div>
      <div class="call-number">1-555-014-2276</div>
    </div>
  </header>

  <nav class="main-nav">
    <a class="nav-item" href="#" style="left:70px;width:220px;">Home</a>
    <a class="nav-item is-active" href="#" style="left:291px;width:252px;">About Bright Lane</a>
    <a class="nav-item" href="#" style="left:560px;width:164px;">Services</a>
    <span class="nav-sep" style="left:724px;"></span>
    <a class="nav-item" href="#" style="left:742px;width:186px;">Our Network</a>
    <span class="nav-sep" style="left:940px;"></span>
    <a class="nav-item" href="#" style="left:960px;width:136px;text-align:right;">Contact Us</a>
  </nav>

  <main>
    <h1 class="page-title">A Few Words About Us</h1>
    <div class="about-photo" role="img" aria-label="Photo of workers raking a lawn in front of a house under a blue sky"></div>
    <h2 class="lead">The founders of Bright Lane Collective have over 30 years in the St. Louis automotive and HVAC industries.</h2>
    <p class="intro-text">In both markets, among many others, one thing is clear: A consumer gets better service at a lower price when they know who to call.&nbsp; Opening up a phonebook, newspaper, or randomly selected online business could cost you hundreds, even thousands of dollars too much money.&nbsp; Sometimes all you really need is a Bright Lane. In both markets, among many others, one thing is clear: A consumer gets better service at a lower price when they know who to call.&nbsp; Opening up a phonebook, newspaper, or randomly selected online business could cost you hundreds, even thousands of dollars too much money.&nbsp; Sometimes all you really need is a Bright Lane.</p>
    <h2 class="section-title">So how good are the Bright Lanes?</h2>
    <p class="body-text">Bright Lane Collective only works with local businesses and individuals that stay true to our mantra.&nbsp; We have a network of literally hundreds of years of experience, and we hold them to the highest of standards.&nbsp; Most importantly we hold them to your standard of excellence.&nbsp; In order maintain good standing in the Bright Lane Collective, every Bright Lane must maintain a customer approval rating of 95%, based on your surveys.</p>
  </main>

  <footer class="site-footer">
    <div class="footer-brand"><span class="brand-dot"></span><span class="brand-name">Bright Lane Collective</span></div>
    <div class="copyright">© copyrights Bright Lane Collective Inc. All rights reserved</div>
    <nav class="footer-nav">
      <a href="#">Home</a><a href="#">About bright lane</a><a href="#">Services</a><a href="#">Our network</a><a href="#">Contact us</a>
    </nav>
    <div class="footer-address">418 Maple Crest Avenue, Riverton, Missouri 63199</div>
    <div class="footer-phone">Phone: 1-555-014-2276</div>
    <div class="footer-email">E-mail: info@brightlanecollective.example</div>
  </footer>
</body>
</html>
```